"Harrow Crest Builders" is a residential building company and needs a new business card design and may re

We would like a redesign based on the existing logo, and would like to see a new font as well. We are bespoke home builders who build sustainable energy efficient homes.

Industry/Entity Type

Construction

Contact Information for Business Card

Business card size 40mm x 90mm

Colors

Designer to choose colors to be used in the design.

```html
<!DOCTYPE html>
<html lang="en">
<head>
<meta charset="utf-8">
<title>Harrow Crest Builders — Business Card</title>
<link rel="stylesheet" href="https://fonts.googleapis.com/css2?family=Exo+2:wght@300;400;600;700&display=swap">
<style>
  :root {
    --page: #f2f2f2;
    --card-centre: #3a393a;
    --card-edge: #1f1e1f;
    --green: #9ac31c;
    --white: #ffffff;
    --grey-text: #d6d6d6;
    --rule: #7a7a7a;
    --badge: #ececec;
  }
  * { box-sizing: border-box; margin: 0; padding: 0; }
  html, body {
    width: 1200px; height: 960px; overflow: hidden;
    background: var(--page);
    font-family: "Exo 2", sans-serif;
  }
  .sheet {
    width: 1200px; height: 960px;
    display: flex; flex-direction: column;
    align-items: center; justify-content: center; gap: 60px;
  }
  .card {
    position: relative;
    width: 900px; height: 400px;
    background: radial-gradient(ellipse at 45% 40%, var(--card-centre) 0%, var(--card-edge) 90%);
    box-shadow: 0 6px 18px rgba(0,0,0,0.18);
    overflow: hidden;
  }

  /* Brand name lockup */
  .brand {
    display: flex; align-items: center; gap: 18px;
    color: var(--white); font-weight: 300; line-height: 1;
  }
  .brand-square {
    background: var(--green);
    flex: none;
  }

  /* Front */
  .card-front {
    display: flex; align-items: center; justify-content: center;
  }
  .card-front .brand { font-size: 58px; letter-spacing: 1px; }
  .card-front .brand-square { width: 56px; height: 56px; }

  /* Back */
  .card-back .brand {
    position: absolute; left: 60px; top: 48px;
    font-size: 34px; gap: 12px;
  }
  .card-back .brand-square { width: 32px; height: 32px; }

  .contact {
    position: absolute; left: 60px; top: 128px;
    color: var(--grey-text); font-size: 19px; line-height: 1.42;
  }
  .contact-name {
    font-size: 26px; font-weight: 700; color: var(--white);
  }
  .contact-name .surname { color: var(--green); }
  .contact-phone {
    font-size: 26px; font-weight: 300; color: var(--green);
    padding-bottom: 8px;
    border-bottom: 1px solid var(--rule);
    width: 300px; margin-bottom: 10px;
  }
  .contact-web { color: var(--green); }

  .accent-bar {
    position: absolute; left: 0; bottom: 34px;
    width: 400px; height: 11px;
    background: var(--green);
  }
  .member-badge {
    position: absolute; right: 56px; bottom: 34px;
    width: 150px; height: 74px;
    background: var(--badge);
    border: 3px solid var(--white);
  }
</style>
</head>
<body>
<main class="sheet">

  <section class="card card-front" aria-label="Business card front">
    <div class="brand">
      <span class="brand-square"></span>
      <span class="brand-name">Harrow Crest Builders</span>
    </div>
  </section>

  <section class="card card-back" aria-label="Business card back">
    <div class="brand">
      <span class="brand-square"></span>
      <span class="brand-name">Harrow Crest Builders</span>
    </div>

    <div class="contact">
      <p class="contact-name">Daniel <span class="surname">Rourke</span></p>
      <p class="contact-phone">0412 587 309</p>
      <p class="contact-address">PO Box 7714 Eastgate LPO Bellmont WA 6104</p>
      <p class="contact-email">daniel@harrowcrestbuilders.com.au</p>
      <p class="contact-web">www.harrowcrestbuilders.com.au</p>
      <p class="contact-reg">Registration 10482 ABN: 47 203 615 882</p>
    </div>

    <div class="accent-bar"></div>
    <div class="member-badge" role="img" aria-label="Industry association membership badge"></div>
  </section>

</main>
</body>
</html>
```